Banner Ad Design Project

I have a digital X Ray blog. I need a header to fit my WP theme.
Please visit the site and let me know what you think. I am open to other design ideas not only the banner. I want the to be clean and professional.

Thank you
www.CordlessPlateScan.com

Target Market(s)

Medical Doctors, Orthopedic Surgeon, X-Ray equipment Dealers,

Industry/Entity Type

Digital

```html
<!DOCTYPE html>
<html lang="en">
<head>
<meta charset="utf-8">
<title>Wireless Digital X-ray Flat Panel Detector – Banner</title>
<link rel="stylesheet" href="https://fonts.googleapis.com/css2?family=Arimo:ital,wght@1,700&display=swap">
<style>
  :root {
    --page-bg: #ffffff;
    --frame: #2a2a2a;
    --band-dark: #2e2e2e;
    --band-mid: #6a6a6a;
    --lower-dark: #7a7a7a;
    --lower-light: #d4d4d4;
    --swoosh: #111111;
    --right-light: #f4f4f4;
    --right-mid: #cfcfcf;
    --headline: #ffffff;
    --tagline: #111111;
    --chevron: #8a8a8a;
    --tile-border: #9a9a9a;
    --tile-bg: #ffffff;
  }
  html, body {
    margin: 0;
    width: 1200px;
    height: 900px;
    overflow: hidden;
    background: var(--page-bg);
  }
  .canvas {
    position: relative;
    width: 1200px;
    height: 900px;
  }
  .banner {
    position: absolute;
    left: 16px;
    top: 360px;
    width: 1168px;
    height: 176px;
    box-sizing: border-box;
    border: 2px solid var(--frame);
    overflow: hidden;
    font-family: "Arimo", Arial, sans-serif;
    font-style: italic;
    font-weight: 700;
  }
  .banner-art {
    position: absolute;
    inset: 0;
    width: 100%;
    height: 100%;
  }
  .headline {
    position: absolute;
    left: 24px;
    top: 22px;
    margin: 0;
    font-size: 27px;
    color: var(--headline);
    letter-spacing: 0.2px;
    text-shadow: 1px 1px 2px rgba(0,0,0,0.6);
  }
  .tagline {
    position: absolute;
    left: 40px;
    top: 100px;
    margin: 0;
    font-size: 35px;
    color: var(--tagline);
    text-shadow: 1px 1px 1px rgba(255,255,255,0.35);
  }
  .chevrons {
    position: absolute;
    left: 824px;
    top: 80px;
    width: 36px;
    height: 20px;
  }
  .product-tile {
    position: absolute;
    top: 24px;
    height: 124px;
    box-sizing: border-box;
    border: 2px solid var(--tile-border);
    background: var(--tile-bg);
    padding: 6px;
  }
  .product-tile--open { left: 876px; width: 118px; }
  .product-tile--front { left: 1004px; width: 154px; }
  .product-photo {
    width: 100%;
    height: 100%;
  }
  .product-tile--open .product-photo {
    background: linear-gradient(160deg, #e6e6e6 0%, #bdbdbd 55%, #3a3a3a 100%);
  }
  .product-tile--front .product-photo {
    background: linear-gradient(135deg, #4a4a4a 0%, #0d0d0d 60%, #262626 100%);
  }
</style>
</head>
<body>
<div class="canvas">
  <section class="banner">
    <svg class="banner-art" viewBox="0 0 1164 172" preserveAspectRatio="none" aria-hidden="true">
      <defs>
        <linearGradient id="rightFill" x1="0" y1="0" x2="1" y2="0">
          <stop offset="0" stop-color="var(--right-mid)"/>
          <stop offset="0.35" stop-color="var(--right-light)"/>
          <stop offset="1" stop-color="var(--right-mid)"/>
        </linearGradient>
        <linearGradient id="bandFill" x1="0" y1="0" x2="1" y2="0">
          <stop offset="0" stop-color="var(--band-dark)"/>
          <stop offset="1" stop-color="var(--band-mid)"/>
        </linearGradient>
        <linearGradient id="lowerFill" x1="0" y1="0" x2="1" y2="0">
          <stop offset="0" stop-color="var(--lower-dark)"/>
          <stop offset="1" stop-color="var(--lower-light)"/>
        </linearGradient>
      </defs>
      <rect class="right-field" width="1164" height="172" fill="url(#rightFill)"/>
      <path class="lower-field" d="M0 70 H720 C700 110 680 140 640 172 H0 Z" fill="url(#lowerFill)"/>
      <path class="swoosh" d="M730 0 H790 C760 70 730 130 680 172 H620 C680 130 720 80 730 0 Z" fill="var(--swoosh)"/>
      <path class="top-band" d="M0 0 H740 C735 30 728 52 718 72 H0 Z" fill="url(#bandFill)"/>
    </svg>

    <h1 class="headline">Wireless Digital X-ray Flat Panel Detector</h1>
    <p class="tagline">The Simple way to upgrade to DR</p>

    <svg class="chevrons" viewBox="0 0 36 20" aria-hidden="true">
      <path d="M2 3 L9 10 L2 17 M12 3 L19 10 L12 17 M22 3 L29 10 L22 17" fill="none" stroke="var(--chevron)" stroke-width="4"/>
    </svg>

    <div class="product-tile product-tile--open">
      <div class="product-photo" role="img" aria-label="Flat panel detector shown open in its carry case"></div>
    </div>
    <div class="product-tile product-tile--front">
      <div class="product-photo" role="img" aria-label="Front view of the black wireless flat panel detector"></div>
    </div>
  </section>
</div>
</body>
</html>
```